Building Servicess

We need a new business card design for a company. We specialise in: Electrical/Site temporary electrics, Data/Network Installation, Passive Fire Protection

Industry/Entity Type

Construction

Contact Information for Business Card

Services provided as detailed on project description

Font styles to use
Serif

Colors
0054AA
0677BA
7BADD7
CADEEF
E8F1F8
00AB8E
00BBA5
67D7C9
C6EFE9
E9F9F6
EB3D1F
EC4F4E
F09395
F8D3D4
FCEDEE

Requirements
Must have
• Company logo-contact details-phone numbers

```html
<!DOCTYPE html>
<html lang="en">
<head>
<meta charset="utf-8">
<title>Northgate Site Services – Business Card</title>
<link rel="stylesheet" href="https://fonts.googleapis.com/css2?family=Montserrat:wght@600;700&family=Questrial&display=swap">
<style>
  :root {
    --page: #eef0f3;
    --navy-deep: #1b202c;
    --navy-mid: #2b3447;
    --steel-grey: #8c9097;
    --brand-blue: #0677ba;
    --bright-blue: #1a8fe0;
    --glass-blue: #0054aa;
    --glass-dark: #0a2a6e;
    --night-black: #050608;
    --night-blue: #0c2740;
    --text-light: #eef1f6;
  }
  * { box-sizing: border-box; margin: 0; padding: 0; }
  html, body { width: 1200px; height: 800px; overflow: hidden; }
  body { background: var(--page); position: relative; }

  .card {
    position: absolute;
    top: 225px;
    width: 540px;
    height: 350px;
    overflow: hidden;
    box-shadow: 0 10px 28px rgba(0,0,0,0.18);
  }
  .card--front { left: 45px; background: linear-gradient(135deg, var(--navy-mid) 0%, var(--navy-deep) 70%); }
  .card--back { left: 615px; }

  .card__chevron { position: absolute; inset: 0; width: 100%; height: 100%; }

  .holder { position: absolute; left: 62px; top: 58px; }
  .holder__name {
    font-family: "Montserrat", sans-serif;
    font-weight: 700;
    font-size: 17px;
    letter-spacing: 0.3px;
    color: var(--bright-blue);
    text-transform: uppercase;
  }
  .holder__role {
    font-family: "Questrial", sans-serif;
    font-size: 15px;
    color: var(--text-light);
    text-transform: uppercase;
    margin-top: 2px;
  }

  .contact { position: absolute; left: 40px; top: 216px; list-style: none; }
  .contact__item {
    display: flex;
    align-items: center;
    gap: 10px;
    height: 36px;
    font-family: "Questrial", sans-serif;
    font-size: 15px;
    color: var(--text-light);
  }
  .contact__icon { width: 16px; height: 16px; flex: none; }

  .night-scene {
    position: absolute; inset: 0;
    background:
      radial-gradient(ellipse 70% 45% at 50% 72%, rgba(40,110,170,0.55), transparent 70%),
      linear-gradient(180deg, var(--night-black) 0%, var(--night-black) 30%, var(--night-blue) 62%, #13314a 100%);
  }
  .company {
    position: absolute;
    left: 0; right: 0; top: 150px;
    text-align: center;
    font-family: "Montserrat", sans-serif;
    font-weight: 700;
    font-size: 26px;
    letter-spacing: 1px;
    color: var(--bright-blue);
    text-transform: uppercase;
  }
</style>
</head>
<body>

  <section class="card card--front" aria-label="Business card front">
    <svg class="card__chevron" viewBox="0 0 540 350" aria-hidden="true">
      <defs>
        <linearGradient id="glass" x1="0" y1="1" x2="1" y2="0">
          <stop offset="0" stop-color="var(--glass-dark)"/>
          <stop offset="0.55" stop-color="var(--glass-blue)"/>
          <stop offset="1" stop-color="#3f8fe6"/>
        </linearGradient>
      </defs>
      <polygon points="450,0 540,0 540,350 300,350 192,266" fill="var(--steel-grey)"/>
      <polygon points="462,0 540,0 540,350 312,350 204,266" fill="var(--navy-deep)"/>
      <polygon points="474,0 540,0 540,350 324,350 216,266" fill="var(--bright-blue)"/>
    </svg>
    <svg class="card__chevron" viewBox="0 0 540 350" role="img" aria-label="Photo of blue glass office towers">
      <polygon points="500,0 540,0 540,350 350,350 244,266" fill="url(#glass)"/>
    </svg>

    <div class="holder">
      <p class="holder__name">Marek Dolan</p>
      <p class="holder__role">Managing Director</p>
    </div>

    <ul class="contact">
      <li class="contact__item">
        <svg class="contact__icon" viewBox="0 0 16 16" aria-hidden="true"><path d="M3.5 1.5l2.2 2.6-1.3 1.6c.9 2 2.4 3.5 4.4 4.4l1.6-1.3 2.6 2.2-1.2 2.3C7 13 3 9 1.7 3.1z" fill="var(--bright-blue)"/></svg>
        07700 900314
      </li>
      <li class="contact__item">
        <svg class="contact__icon" viewBox="0 0 16 16" aria-hidden="true"><rect x="4" y="1" width="8" height="14" rx="1.5" fill="none" stroke="var(--bright-blue)" stroke-width="1.6"/><circle cx="8" cy="12.4" r="0.9" fill="var(--bright-blue)"/></svg>
        020 7946 0381
      </li>
      <li class="contact__item">
        <svg class="contact__icon" viewBox="0 0 16 16" aria-hidden="true"><circle cx="8" cy="8" r="7" fill="var(--bright-blue)"/><path d="M1 8h14M8 1c-2.5 2.2-2.5 11.8 0 14M8 1c2.5 2.2 2.5 11.8 0 14" fill="none" stroke="var(--navy-deep)" stroke-width="1"/></svg>
        www.northgatesite.co.uk
      </li>
    </ul>
  </section>

  <section class="card card--back" aria-label="Business card back">
    <div class="night-scene" role="img" aria-label="Photo of a city skyline lit up at night"></div>
    <p class="company">Northgate Site Services Ltd</p>
  </section>

</body>
</html>
```